Redesign the content on our home page

Thanks for your designs thus far.

There have been a few requests for feedback, so I have mocked up another layout. I am happy with everything except the 6 boxes in the green square. This is the piece I need the perfect design for.
- What the boxes look like
- Icons to be used
- Colours
- etc

__________________________________________________________________

We have the basic layout for our homepage, the header and footer are done. Please see attached (Homepage)

Only design in PSD etc needed, no coding. Also, header and footer not needed either, only formatting and graphic design of home page content. See eps file for the information.

I need more information added to the homepage and displayed in an organised way and designed so it presents well.

Our slogan is "Travel Insurance made simple". Therefore the design needs to represent this by being a simple, clear and clean layout of information. Website visitors need to be able to access and digest the information fast and this is reliant on the design of the information.

Attached is a mock up with all of the information.

Please ask and questions you need to help with the design.

Project Deadline Extended Reason: Deadline has been extended to provide further clarification for the required design.I need the 6 boxes inside the green outline designed. The design of the 6 boxes should be simple and follow the pages design and be simple in appearance. Thanks for your designs thus far. Added Thursday, October 8, 2015

Target Market(s)

Mostly female, any age.

Industry/Entity Type

Travel

Number of Pages Required

1 page

Font styles to use
Other font styles liked:
• MetaPro

Colors
f37122
33a6d7
33b8a4
dbdbdb
606060

Requirements
Must have
• - Follow home page look and feel
• - Simple design
• - Fast for a visitor to digest the information
Nice to have
• Simple design. Webpage is responsive so elements should look good when scaled for mobile.
Should not have
• No new colours to be introduced then what is in the design already or selected below.
• No new fonts.

```html
<!DOCTYPE html>
<html lang="en">
<head>
<meta charset="utf-8">
<title>Swiftway Travel Insurance</title>
<link href="https://fonts.googleapis.com/css2?family=Open+Sans:wght@400;600;700;800&display=swap" rel="stylesheet">
<style>
:root{
  --orange:#f37122;
  --orange-dark:#d95c12;
  --blue:#33a6d7;
  --teal:#33b8a4;
  --grey-light:#dbdbdb;
  --grey:#606060;
  --red:#e2453c;
  --white:#ffffff;
  --paper:#f5f5f5;
}
*{box-sizing:border-box;margin:0;padding:0}
html,body{width:1200px;height:2500px;overflow:hidden;background:var(--white)}
body{font-family:"Open Sans",Arial,sans-serif;color:var(--grey)}
.page{width:1200px;height:2500px;position:relative;overflow:hidden}

/* header */
.site-header{height:64px;display:flex;align-items:center;justify-content:space-between;padding:0 48px;background:var(--white);border-bottom:1px solid var(--grey-light)}
.brand{display:flex;flex-direction:column}
.brand-name{font-size:30px;font-weight:800;color:var(--orange);line-height:1}
.brand-tag{font-size:10px;color:var(--grey);margin-top:2px}
.header-right{display:flex;flex-direction:column;align-items:flex-end;gap:6px}
.header-phone{font-size:12px;font-weight:700;color:var(--orange);display:flex;align-items:center;gap:5px}
.main-nav{display:flex;gap:28px}
.main-nav a{font-size:12px;font-weight:700;color:var(--orange);text-decoration:none;text-transform:uppercase}

/* hero */
.hero{height:446px;background:radial-gradient(ellipse at 50% 30%,#f78a45 0%,var(--orange) 55%,var(--orange-dark) 100%);position:relative;text-align:center;color:var(--white)}
.hero-kicker{padding-top:24px;font-size:13px;font-weight:600;letter-spacing:1px;opacity:.8;text-transform:uppercase}
.hero-title{margin-top:22px;display:flex;justify-content:center;align-items:center;gap:16px}
.hero-title h1{font-size:44px;font-weight:800;text-transform:uppercase}
.field{background:var(--white);border-radius:4px;height:46px;display:inline-flex;align-items:center;padding:0 12px;gap:10px}
.field-dest{width:160px}
.field-go{width:26px;height:26px;border-radius:4px;background:var(--blue);margin-left:auto}
.hero-dates{margin-top:16px;display:flex;justify-content:center;align-items:center;gap:14px;font-size:34px;font-weight:800}
.field-date{width:130px;height:40px}
.multi-trip{margin:22px auto 0;width:440px;height:36px;background:var(--blue);border-radius:4px;font-size:12px;font-weight:700;display:flex;align-items:center;justify-content:center;gap:10px}
.multi-trip .box{width:14px;height:14px;border:2px solid var(--white);border-radius:2px}
.hero-art{position:absolute;left:0;right:0;bottom:0;height:170px;background:linear-gradient(180deg,rgba(217,92,18,0) 0%,rgba(190,76,14,.55) 100%)}
.hero-arrow{position:absolute;top:190px;width:40px;height:40px;border-radius:50%;border:2px solid rgba(255,255,255,.7);display:flex;align-items:center;justify-content:center}
.hero-arrow.left{left:40px}.hero-arrow.right{right:40px}
.underwriter{position:absolute;right:60px;bottom:30px;display:flex;align-items:center;gap:8px;font-size:20px;font-weight:700;color:var(--white)}
.underwriter .dot{width:16px;height:16px;border-radius:50%;background:var(--white)}

/* sections */
.section{text-align:center}
.section h2{font-size:26px;font-weight:800;color:var(--grey);text-transform:uppercase}
.lede{font-size:12px;max-width:700px;margin:10px auto 0;line-height:1.6}
.features{display:flex;justify-content:center;gap:40px;margin-top:36px}
.feature{width:200px;text-align:center}
.feature-icon{width:96px;height:96px;border-radius:50%;margin:0 auto;display:flex;align-items:center;justify-content:center}
.feature h3{font-size:14px;font-weight:800;text-transform:uppercase;color:var(--grey);margin-top:16px;line-height:1.3}
.feature p{font-size:11px;line-height:1.55;margin-top:8px}
.read-more{display:block;font-size:11px;font-weight:700;color:var(--blue);margin-top:8px;text-transform:uppercase}
.bg-blue{background:var(--blue)}.bg-red{background:var(--red)}.bg-teal{background:var(--teal)}.bg-orange{background:var(--orange)}

.simple{padding-top:52px;height:480px}
.btn-outline{display:inline-block;margin-top:32px;padding:9px 26px;border:1px solid var(--grey);font-size:11px;font-weight:700;color:var(--grey);text-transform:uppercase}

.award{height:160px;background:var(--teal);color:var(--white);display:flex;align-items:center;padding:0 150px;gap:60px;margin-top:30px}
.award-badge{width:170px;height:70px;border-radius:8px;background:var(--white)}
.award h2{font-size:24px;font-weight:800;text-transform:uppercase}
.award ul{list-style:none;margin-top:10px}
.award li{font-size:13px;display:flex;align-items:center;gap:8px;margin-top:4px}

.confidence{padding-top:40px;height:390px}
.confidence .feature-icon{width:110px;height:110px;background:var(--white);border:3px solid var(--grey-light)}

.rating{height:50px;background:var(--blue);color:var(--white);font-size:13px;font-weight:700;display:flex;align-items:center;justify-content:center;text-transform:uppercase;letter-spacing:.3px}

.resources{padding-top:34px;height:240px}
.resources .features{margin-top:0;gap:90px}
.resources .feature{width:240px}
.resources .feature-icon{width:80px;height:80px}

.partners{height:90px;background:var(--paper);display:flex;align-items:center;justify-content:center;gap:50px}
.partner{width:120px;height:40px;border-radius:6px;background:var(--grey-light)}

/* footer */
.site-footer{border-top:5px solid var(--orange);height:290px;display:flex;padding:30px 70px 0;gap:60px}
.footer-brand .brand-name{font-size:34px}
.footer-col{flex:1;font-size:11px;line-height:1.6}
.footer-col h4{background:var(--orange);color:var(--white);font-size:12px;font-weight:800;padding:7px 12px;text-transform:uppercase;margin-bottom:12px}
.footer-col p{padding:0 12px 8px}
.legal{padding:0 70px;font-size:10px;line-height:1.7;color:#888}
.legal .copy{text-align:center;margin-top:10px}
</style>
</head>
<body>
<div class="page">

<header class="site-header">
  <div class="brand">
    <span class="brand-name">Swiftway</span>
    <span class="brand-tag">Travel insurance made simple</span>
  </div>
  <div class="header-right">
    <span class="header-phone">
      <svg width="12" height="12" viewBox="0 0 24 24"><path fill="#f37122" d="M6.6 10.8a15 15 0 0 0 6.6 6.6l2.2-2.2a1 1 0 0 1 1-.2 11 11 0 0 0 3.6.6 1 1 0 0 1 1 1V20a1 1 0 0 1-1 1A17 17 0 0 1 3 4a1 1 0 0 1 1-1h3.5a1 1 0 0 1 1 1c0 1.2.2 2.4.6 3.6a1 1 0 0 1-.3 1z"/></svg>
      1300 555 018
    </span>
    <nav class="main-nav">
      <a>Travel Insurance</a><a>What we cover</a><a>Your policy</a><a>FAQ</a><a>Emergency</a>
    </nav>
  </div>
</header>

<section class="hero">
  <p class="hero-kicker">Stop settling for less. Get your travel insurance quote now</p>
  <div class="hero-title">
    <h1>I'm travelling to</h1>
    <span class="field field-dest"><span class="field-go"></span></span>
  </div>
  <div class="hero-dates">
    <span>FROM</span><span class="field field-date"></span>
    <span>TILL</span><span class="field field-date"></span>
  </div>
  <div class="multi-trip"><span class="box"></span>I'M TRAVELLING MULTIPLE TIMES IN THE YEAR</div>
  <div class="hero-art" role="img" aria-label="Illustrated city skyline with a traveller holding a suitcase"></div>
  <span class="hero-arrow left"><svg width="14" height="14" viewBox="0 0 14 14"><path d="M9 2 4 7l5 5" stroke="#fff" stroke-width="2" fill="none"/></svg></span>
  <span class="hero-arrow right"><svg width="14" height="14" viewBox="0 0 14 14"><path d="m5 2 5 5-5 5" stroke="#fff" stroke-width="2" fill="none"/></svg></span>
  <div class="underwriter"><span class="dot"></span>Meridian</div>
</section>

<section class="section simple">
  <h2>Travel insurance made simple</h2>
  <p class="lede">We don't believe in making things complicated, so we've made travel insurance simple, fast and easy to understand from the moment you get a quote.</p>
  <div class="features">
    <div class="feature">
      <div class="feature-icon bg-blue"><svg width="46" height="46" viewBox="0 0 24 24"><circle cx="12" cy="12" r="9" stroke="#fff" stroke-width="2" fill="none"/><path d="M12 7v5l3 2" stroke="#fff" stroke-width="2" fill="none"/></svg></div>
      <h3>Fast and simple<br>instant quotes</h3>
      <p>Get a price in seconds with only a few questions about your trip and travellers.</p>
      <span class="read-more">Read more ›</span>
    </div>
    <div class="feature">
      <div class="feature-icon bg-red"><svg width="46" height="46" viewBox="0 0 24 24"><path d="M9 3h6v6h6v6h-6v6H9v-6H3V9h6z" fill="#fff"/></svg></div>
      <h3>No medical<br>assessments</h3>
      <p>Many existing conditions are covered automatically with no forms to complete.</p>
      <span class="read-more">Read more ›</span>
    </div>
    <div class="feature">
      <div class="feature-icon bg-teal"><svg width="46" height="46" viewBox="0 0 24 24"><path d="M3 4h3l2 11h11l2-8H7" stroke="#fff" stroke-width="2" fill="none"/><circle cx="9" cy="19" r="1.6" fill="#fff"/><circle cx="17" cy="19" r="1.6" fill="#fff"/></svg></div>
      <h3>Fast and simple<br>purchase</h3>
      <p>Buy your policy online in minutes and receive your documents straight away.</p>
      <span class="read-more">Read more ›</span>
    </div>
    <div class="feature">
      <div class="feature-icon bg-orange"><svg width="46" height="46" viewBox="0 0 24 24"><rect x="4" y="5" width="16" height="11" rx="1" stroke="#fff" stroke-width="2" fill="none"/><path d="M2 19h20" stroke="#fff" stroke-width="2"/></svg></div>
      <h3>Simple online<br>claims</h3>
      <p>Lodge a claim online at any time and track its progress from anywhere.</p>
      <span class="read-more">Read more ›</span>
    </div>
  </div>
  <span class="btn-outline">View more</span>
</section>

<section class="award">
  <div class="award-badge"></div>
  <div>
    <h2>Award winning travel insurance</h2>
    <ul>
      <li><svg width="14" height="14" viewBox="0 0 14 14"><path d="m2 7 3 3 7-7" stroke="#fff" stroke-width="2" fill="none"/></svg>Best Value Comprehensive cover</li>
      <li><svg width="14" height="14" viewBox="0 0 14 14"><path d="m2 7 3 3 7-7" stroke="#fff" stroke-width="2" fill="none"/></svg>Best Value Basic cover</li>
    </ul>
  </div>
</section>

<section class="section confidence">
  <h2>Travel with confidence</h2>
  <p class="lede">Wherever you are travelling, you want to feel sure that help is close by. Our policies are backed by a trusted insurer and a team ready to support you around the clock.</p>
  <div class="features">
    <div class="feature">
      <div class="feature-icon"><svg width="50" height="50" viewBox="0 0 24 24"><path d="M12 2 4 5v6c0 5 3.5 9 8 11 4.5-2 8-6 8-11V5z" fill="#33b8a4"/><path d="m8 12 3 3 5-6" stroke="#fff" stroke-width="2" fill="none"/></svg></div>
      <p>When you travel with us, we cover you from the moment your policy is issued.</p>
      <span class="read-more">Read more ›</span>
    </div>
    <div class="feature">
      <div class="feature-icon"><svg width="50" height="50" viewBox="0 0 24 24"><circle cx="12" cy="12" r="9" fill="#33a6d7"/></svg></div>
      <p>Travel with confidence knowing your policy is underwritten by Meridian.</p>
      <span class="read-more">Read more ›</span>
    </div>
    <div class="feature">
      <div class="feature-icon"><svg width="50" height="50" viewBox="0 0 24 24"><rect x="3" y="5" width="18" height="14" rx="2" fill="#e2453c"/><path d="M7 12h10" stroke="#fff" stroke-width="2"/></svg></div>
      <p>The price of your quote is locked in for 48 hours after you receive it.</p>
      <span class="read-more">Read more ›</span>
    </div>
    <div class="feature">
      <div class="feature-icon"><svg width="50" height="50" viewBox="0 0 24 24"><circle cx="12" cy="12" r="9" fill="#f37122"/><path d="M12 7v5l3 2" stroke="#fff" stroke-width="2" fill="none"/></svg></div>
      <p>Change your mind? You can cancel your policy within the cooling off period.</p>
      <span class="read-more">Read more ›</span>
    </div>
  </div>
</section>

<div class="rating">Swiftway travel insurance is rated 4.1 stars by 25 customers on Review Hub as at 1/8/15</div>

<section class="section resources">
  <div class="features">
    <div class="feature">
      <div class="feature-icon bg-red"><svg width="38" height="38" viewBox="0 0 24 24"><path d="M12 3 2 21h20z" fill="#fff"/><path d="M12 10v5" stroke="#e2453c" stroke-width="2"/><circle cx="12" cy="18" r="1" fill="#e2453c"/></svg></div>
      <h3>Travel alerts</h3>
      <p>Stay informed about events around the world that may affect your travel plans.</p>
    </div>
    <div class="feature">
      <div class="feature-icon bg-blue"><svg width="38" height="38" viewBox="0 0 24 24"><path d="M12 2a7 7 0 0 0-7 7c0 5 7 13 7 13s7-8 7-13a7 7 0 0 0-7-7z" fill="#fff"/><circle cx="12" cy="9" r="2.5" fill="#33a6d7"/></svg></div>
      <h3>Travel guides</h3>
      <p>Helpful tips for every destination so you can plan your next trip with ease.</p>
    </div>
    <div class="feature">
      <div class="feature-icon bg-teal"><svg width="38" height="38" viewBox="0 0 24 24"><rect x="4" y="4" width="16" height="16" rx="2" fill="#fff"/><path d="M8 9h8M8 12h8M8 15h5" stroke="#33b8a4" stroke-width="1.6"/></svg></div>
      <h3>Travel blog</h3>
      <p>Read the latest stories and ideas from our team to inspire your adventures.</p>
    </div>
  </div>
</section>

<div class="partners">
  <span class="partner"></span><span class="partner"></span><span class="partner"></span><span class="partner"></span><span class="partner"></span><span class="partner"></span>
</div>

<footer class="site-footer">
  <div class="footer-brand brand">
    <span class="brand-name">Swiftway</span>
    <span class="brand-tag">Travel insurance made simple</span>
  </div>
  <div class="footer-col">
    <h4>Sales &amp; general enquiries</h4>
    <p>1300 555 018<br>hello@swiftway.example<br>Fax (02) 5550 1120</p>
    <p>Swiftway Travel Insurance<br>PO Box 0000<br>Harbour City NSW 2000</p>
  </div>
  <div class="footer-col">
    <h4>Claims</h4>
    <p>1300 555 019<br>claims@swiftway.example<br>Fax (02) 5550 1121</p>
    <p>Swiftway Claims<br>PO Box 0001<br>Harbour City NSW 2000</p>
  </div>
  <div class="footer-col">
    <h4>Administration</h4>
    <p>(02) 5550 1122<br>admin@swiftway.example<br>Fax (02) 5550 1123</p>
    <p>Level 10, 1 Example Street<br>Harbour City NSW 2000</p>
  </div>
</footer>

<div class="legal">
  <p>Swiftway Pty Ltd is an authorised representative of Meridian. Insurance is issued and managed by Meridian under its licence. Any advice on this website is general only and does not consider your objectives, financial situation or needs. Please read the Product Disclosure Statement before deciding whether this product is right for you. If you purchase a policy, we receive a commission which is a percentage of your premium. Ask us for more information.</p>
  <p class="copy">© Swiftway 2015. All rights reserved.</p>
</div>

</div>
</body>
</html>
```